VERIDAX Need a luxury modern business card designed.

Need a luxury modern business card designed. refer to the uploaded files for the company name and logo in the zip file under source files. i will making my descion on monday. so please send in before then so if we need to edit we will have the time. we have a trade show coming up and im on a deadline for printer.

Target Market(s)

high end clients

Contact Information for Business Card

Company nAme and logo. Calvin Ostrow Co-Founder / Project Manager Office # 416-555-0193 Cell # 416-555-0147 VERIDAX.CA Calvin@veridax.ca

Font styles to use
Other font styles liked:
• Modern

Requirements
Must have
• Company name and logo, contact info, using the black, gold and white color scheme.

```html
<!DOCTYPE html>
<html lang="en">
<head>
<meta charset="utf-8">
<title>VERIDAX Business Card</title>
<link rel="stylesheet" href="https://fonts.googleapis.com/css2?family=Josefin+Sans:wght@300;400&display=swap">
<style>
  :root {
    --backdrop: #a3a3a3;
    --card: #202223;
    --card-edge: #2a2c2d;
    --white: #ecebe6;
    --soft-white: #c9c8c3;
    --gold: #8c7f4f;
  }
  * { margin: 0; padding: 0; box-sizing: border-box; }
  html, body {
    width: 1200px;
    height: 787px;
    overflow: hidden;
  }
  body {
    background: var(--backdrop);
    font-family: "Josefin Sans", "Century Gothic", sans-serif;
    font-weight: 300;
    display: flex;
    align-items: center;
    justify-content: center;
    gap: 56px;
  }
  .card {
    position: relative;
    width: 520px;
    height: 297px;
    background: var(--card);
    border: 1px solid var(--card-edge);
    color: var(--white);
  }

  /* Brand face */
  .brand {
    position: absolute;
    left: 0; right: 0;
    top: 108px;
    display: flex;
    flex-direction: column;
    align-items: center;
  }
  .brand-name {
    display: flex;
    align-items: center;
    gap: 10px;
    font-size: 26px;
    letter-spacing: 7px;
    color: var(--white);
    line-height: 1;
  }
  .brand-mark {
    width: 9px;
    height: 9px;
    background: var(--gold);
  }
  .brand-rule {
    width: 190px;
    height: 1px;
    background: var(--soft-white);
    margin: 9px 0 6px;
  }
  .brand-tagline {
    font-size: 8px;
    letter-spacing: 3px;
    color: var(--gold);
  }
  .dots {
    position: absolute;
    left: 50%;
    bottom: 34px;
    transform: translateX(-50%);
    display: flex;
    gap: 5px;
  }
  .dots span {
    width: 4px;
    height: 4px;
    background: var(--white);
  }

  /* Contact face */
  .contact-brand {
    position: absolute;
    top: 34px;
    left: 0; right: 0;
    text-align: center;
    font-size: 12px;
    letter-spacing: 4px;
    color: var(--white);
  }
  .person {
    position: absolute;
    left: 34px;
    top: 128px;
  }
  .person-name {
    font-size: 14px;
    letter-spacing: 1.5px;
    color: var(--white);
  }
  .person-role {
    font-size: 11px;
    letter-spacing: 1px;
    color: var(--soft-white);
    margin-top: 3px;
  }
  .details {
    position: absolute;
    right: 34px;
    top: 122px;
    list-style: none;
    font-size: 11px;
    letter-spacing: 1px;
    color: var(--white);
    text-align: right;
  }
  .details li {
    display: flex;
    align-items: center;
    justify-content: flex-end;
    gap: 5px;
    margin-bottom: 4px;
  }
  .details svg {
    width: 9px;
    height: 9px;
    stroke: var(--white);
    fill: none;
    stroke-width: 1.2;
  }
  .address {
    position: absolute;
    right: 34px;
    bottom: 26px;
    font-size: 11px;
    letter-spacing: 1px;
    color: var(--soft-white);
  }
</style>
</head>
<body>
  <section class="card card-brand">
    <div class="brand">
      <div class="brand-name"><span class="brand-mark"></span>VERIDAX</div>
      <div class="brand-rule"></div>
      <div class="brand-tagline">LUXURY LANDSCAPES</div>
    </div>
    <div class="dots"><span></span><span></span><span></span><span></span><span></span></div>
  </section>

  <section class="card card-contact">
    <div class="contact-brand">VERIDAX</div>
    <div class="person">
      <div class="person-name">Name Name</div>
      <div class="person-role">Position</div>
    </div>
    <ul class="details">
      <li>
        <svg viewBox="0 0 10 10"><path d="M2 1 L4 1 L4.6 3 L3.4 4 Q4.5 6 6 6.6 L7 5.4 L9 6 L9 8 Q5 9 2.5 6 Q1 4 2 1 Z"/></svg>
        000 0000 0000
      </li>
      <li>
        <svg viewBox="0 0 10 10"><rect x="1" y="2" width="8" height="6"/><path d="M1 2 L5 5.5 L9 2"/></svg>
        info@veridax.com
      </li>
      <li>
        <svg viewBox="0 0 10 10"><circle cx="5" cy="5" r="4"/><ellipse cx="5" cy="5" rx="1.8" ry="4"/><path d="M1 5 H9"/></svg>
        www.veridax.com
      </li>
    </ul>
    <div class="address">Address</div>
  </section>
</body>
</html>
```